4x6 -ish post card to let the neighborhood know where here.

Hi All, I opened a high end wine & spirits shop and am looking to get out some sort of a 4x6 postcard a flyer to let people know where in the area. Looking for something clean cut that can maybe incorporate a few pictures from our store on along the top and our logo. Ideally a white-ish background.

```html
<!DOCTYPE html>
<html lang="en">
<head>
<meta charset="utf-8">
<title>Stonebrook Wine &amp; Spirits – Neighborhood Postcard</title>
<link rel="stylesheet" href="https://fonts.googleapis.com/css2?family=Cinzel:wght@500&family=Great+Vibes&family=Poppins:ital,wght@0,400;0,600;0,700;1,300&family=Roboto+Condensed:wght@400&family=Arimo:wght@400;700&display=swap">
<style>
  :root{
    --stage:#afadae;
    --paper:#fffdf6;
    --gold:#c4963a;
    --gold-light:#f6e07a;
    --gold-mid:#e6bf3f;
    --ink:#111111;
    --white:#ffffff;
  }
  *{box-sizing:border-box;margin:0;padding:0}
  html,body{width:1094px;height:1200px;overflow:hidden;background:var(--stage)}
  .card{
    position:absolute;width:720px;height:480px;background:var(--paper);
    overflow:hidden;box-shadow:0 14px 18px -8px rgba(0,0,0,.35);
  }
  .card--front{left:189px;top:84px}
  .card--back{left:185px;top:618px}
  .card svg.art{position:absolute;inset:0;width:720px;height:480px}
  .brand{position:absolute;font-family:"Cinzel",serif;font-weight:500;color:var(--gold);line-height:1;white-space:nowrap}
  .brand__name{display:block;letter-spacing:.5px}
  .brand__line{display:block;letter-spacing:2.4px}
  .card--front .brand{left:52px;top:62px}
  .card--front .brand__name{font-size:25px}
  .card--front .brand__line{font-size:15.5px;margin-top:4px}
  .card--back .brand{left:30px;top:36px}
  .card--back .brand__name{font-size:21px}
  .card--back .brand__line{font-size:13px;margin-top:3px}
  .script{font-family:"Great Vibes",cursive;color:var(--ink);position:absolute;line-height:1;white-space:nowrap}
  .headline__big{left:432px;top:16px;font-size:78px}
  .headline__small{left:428px;top:66px;font-size:56px}
  .tagline{position:absolute;left:430px;top:116px;font-family:"Poppins",sans-serif;font-size:15.5px;color:var(--ink);letter-spacing:.3px;white-space:nowrap}
  .tagline b{font-weight:700}
  .visit{position:absolute;left:26px;top:408px}
  .visit__label{font-family:"Great Vibes",cursive;font-size:26px;color:#333;display:block;line-height:1}
  .visit__url{font-family:"Poppins",sans-serif;font-weight:700;font-size:20px;color:var(--ink);display:block;line-height:1.1;letter-spacing:.3px}
  .back-title{left:402px;top:26px;font-size:54px}
  .contact{position:absolute;left:421px;top:281px;width:262px;font-family:"Poppins",sans-serif;color:var(--gold);text-align:right}
  .contact__call{font-size:25px;line-height:1;white-space:nowrap}
  .contact__call i{font-weight:300}
  .contact__call b{font-weight:700}
  .contact__web{font-size:23px;line-height:1;margin-top:3px;white-space:nowrap}
  .contact__web b{font-weight:700}
  .contact__web span{font-weight:400}
  .address{position:absolute;left:424px;top:330px;width:256px;height:18px;border-radius:9px;background:var(--ink);color:var(--white);font-family:"Roboto Condensed",sans-serif;font-size:12.5px;line-height:18px;text-align:center;white-space:nowrap}
  .mail-box{position:absolute;top:375px;height:76px;border:1px solid #555;background:var(--white);font-family:"Arimo",sans-serif;color:#333}
  .mail-box--address{left:407px;width:189px;font-size:11px}
  .mail-box--address .sort{position:absolute;right:14px;top:8px;font-size:9px}
  .mail-box--address .recipient{position:absolute;left:13px;top:37px;line-height:1.15}
  .mail-box--permit{left:608px;width:76px;font-size:10px;text-align:center;line-height:1.22;padding-top:6px}
  .mail-box--permit b{font-weight:700}
</style>
</head>
<body>

<!-- FRONT -->
<section class="card card--front">
  <svg class="art" viewBox="0 0 720 480">
    <defs>
      <linearGradient id="shelfTone" x1="0" y1="0" x2="0" y2="1">
        <stop offset="0" stop-color="#3a3a3e"/>
        <stop offset=".45" stop-color="#6b4a2c"/>
        <stop offset=".7" stop-color="#2e2d30"/>
        <stop offset="1" stop-color="#7a6040"/>
      </linearGradient>
      <linearGradient id="goldBand" x1="0" y1="0" x2="1" y2="0">
        <stop offset="0" stop-color="var(--gold-mid)"/>
        <stop offset=".5" stop-color="var(--gold-light)"/>
        <stop offset="1" stop-color="var(--gold-mid)"/>
      </linearGradient>
    </defs>
    <rect x="0" y="110" width="720" height="370" fill="url(#shelfTone)" role="img" aria-label="Store photo: shelves of whiskey and spirits above racks of wine bottles"/>
    <path d="M0 0H720V180C650 200 600 205 549 198C450 185 350 120 243 123C150 125 60 150 0 168Z" fill="var(--paper)"/>
    <path d="M0 168C60 150 150 125 243 123C350 120 450 185 549 198C600 205 650 200 720 180V188C650 212 600 216 549 210C450 200 350 142 243 142C150 142 60 168 0 196Z" fill="url(#goldBand)"/>
    <path d="M0 370C160 330 310 390 428 480H405C300 400 150 340 0 378Z" fill="url(#goldBand)"/>
    <path d="M0 378C150 340 300 400 405 480H0Z" fill="var(--paper)"/>
  </svg>

  <div class="brand"><span class="brand__name">STONEBROOK</span><span class="brand__line">WINE &amp; SPIRITS</span></div>

  <div class="script headline__big">Premium</div>
  <div class="script headline__small">wines &amp; spirits</div>
  <p class="tagline">NOW IN <b>YOUR NEIGHBORHOOD</b></p>

  <div class="visit">
    <span class="visit__label">Visit Us</span>
    <span class="visit__url">StonebrookWine.com</span>
  </div>
</section>

<!-- BACK -->
<section class="card card--back">
  <svg class="art" viewBox="0 0 720 480">
    <defs>
      <linearGradient id="portraitTone" x1="0" y1="0" x2="1" y2="1">
        <stop offset="0" stop-color="#5a4232"/>
        <stop offset=".45" stop-color="#c98f74"/>
        <stop offset=".75" stop-color="#d8485a"/>
        <stop offset="1" stop-color="#b8303f"/>
      </linearGradient>
      <linearGradient id="goldBandB" x1="0" y1="0" x2="0" y2="1">
        <stop offset="0" stop-color="var(--gold-mid)"/>
        <stop offset=".5" stop-color="var(--gold-light)"/>
        <stop offset="1" stop-color="var(--gold-mid)"/>
      </linearGradient>
      <linearGradient id="shopTone" x1="0" y1="0" x2="1" y2="1">
        <stop offset="0" stop-color="#2c2b2f"/>
        <stop offset=".6" stop-color="#6a4c35"/>
        <stop offset="1" stop-color="#9b8a7a"/>
      </linearGradient>
      <linearGradient id="frontTone" x1="0" y1="0" x2="0" y2="1">
        <stop offset="0" stop-color="#4a4e58"/>
        <stop offset=".5" stop-color="#e9e8e4"/>
        <stop offset="1" stop-color="#8a7f78"/>
      </linearGradient>
    </defs>
    <path d="M0 180C120 110 240 90 297 0H345C314 80 344 200 402 330C414 400 374 450 357 480H0Z" fill="url(#goldBandB)"/>
    <path d="M0 180C120 110 240 90 283 0H331C300 80 330 200 388 330C400 400 360 450 343 480H0Z" fill="url(#portraitTone)" role="img" aria-label="Photo: smiling woman in a red top tasting a glass of red wine"/>
    <path d="M0 182C120 112 240 92 283 0H300C255 104 130 134 0 206Z" fill="url(#goldBandB)"/>
    <path d="M0 0H283C240 90 120 110 0 180Z" fill="var(--paper)"/>
    <circle cx="454" cy="177" r="78" fill="url(#shopTone)" role="img" aria-label="Store interior photo: wine racks and spirit shelves"/>
    <circle cx="623" cy="177" r="78" fill="url(#frontTone)" role="img" aria-label="Storefront photo: white shop front with Wine &amp; Spirits awning"/>
  </svg>

  <div class="brand"><span class="brand__name">STONEBROOK</span><span class="brand__line">WINE &amp; SPIRITS</span></div>

  <div class="script back-title">Wine &amp; Spirits</div>

  <div class="contact">
    <p class="contact__call"><i>CALL US</i> <b>555.010.482</b></p>
    <p class="contact__web"><b>STONEBROOK</b><span>WINE.COM</span></p>
  </div>
  <p class="address">48 Harbor Lane, Fairview, CT, US 06000</p>

  <div class="mail-box mail-box--address">
    <span class="sort">****************ECRWSS****</span>
    <p class="recipient">Local<br>Postal Customer</p>
  </div>
  <div class="mail-box mail-box--permit">PRSRT STD<br>ECRWSS<br>U.S. Postage<br><b>PAID</b><br>EDDM RETAIL</div>
</section>

</body>
</html>
```